'The Willow Lantern Boutique' Ecommerce boutique (womens clothing) needs a business card design

Ecommerce boutique (womens clothing) needs a business card design, we need a business card that's fresh, innovative, clean design that matches our quality products and attracts quality suppliers as well as customers.
We aim to create a feel good shopping experience that goes past the point of sale.
Updates
Target Market(s)
Women 18-35, fashion forward, disposable income, unique.
Industry/Entity Type
Boutique
Font styles to use
Colors
Designer to choose colors to be used in the design.
Look and feel
Each slider illustrates characteristics of the customer's brand and the style your logo design should communicate.

```html
<!DOCTYPE html>
<html lang="en">
<head>
<meta charset="utf-8">
<title>The Willow Lantern Boutique – Business Card</title>
<link href="https://fonts.googleapis.com/css2?family=Open+Sans:wght@400;600&display=swap" rel="stylesheet">
<style>
  :root {
    --backdrop: #c9c9c9;
    --card: #ffffff;
    --panel: #3a3939;
    --ink: #2e2e2e;
    --light: #ffffff;
    --muted: #d8d8d8;
  }
  html, body {
    margin: 0;
    padding: 0;
    overflow: hidden;
  }
  .canvas {
    width: 1200px;
    height: 896px;
    background: var(--backdrop);
    display: flex;
    align-items: center;
    justify-content: center;
    gap: 40px;
    font-family: "Open Sans", Arial, sans-serif;
  }
  .card {
    position: relative;
    width: 540px;
    height: 310px;
    background: var(--card);
    box-shadow: 0 6px 18px rgba(0,0,0,0.18);
    overflow: hidden;
  }

  /* Front face */
  .front-panel {
    position: absolute;
    top: 14px;
    bottom: 14px;
    left: 150px;
    right: 0;
    background: var(--panel);
    border-radius: 18px 0 0 18px;
    display: flex;
    flex-direction: column;
    align-items: center;
    justify-content: center;
    color: var(--light);
  }
  .brand-name {
    margin: 0;
    font-weight: 400;
    font-size: 30px;
    line-height: 1.15;
    text-align: center;
    letter-spacing: 0.5px;
  }
  .brand-name .brand-sub {
    display: block;
    font-size: 22px;
    letter-spacing: 10px;
    margin-top: 6px;
  }
  .holder {
    position: absolute;
    left: 22px;
    bottom: 24px;
    margin: 0;
    font-size: 14px;
    color: var(--ink);
    white-space: nowrap;
    transform-origin: left bottom;
    transform: rotate(-90deg) translate(0, 100%);
  }
  .holder strong { font-weight: 600; }
  .holder .divider { margin: 0 6px; }

  /* Back face */
  .contact-band {
    position: absolute;
    top: 66px;
    height: 150px;
    left: 12px;
    right: 0;
    background: var(--panel);
    border-radius: 16px 0 0 16px;
    display: flex;
    align-items: center;
    padding-left: 40px;
  }
  .contact-list {
    list-style: none;
    margin: 0;
    padding: 0;
    display: grid;
    grid-template-columns: auto auto;
    column-gap: 22px;
    row-gap: 12px;
    color: var(--muted);
    font-size: 11px;
  }
  .contact-list li {
    display: flex;
    align-items: center;
    gap: 6px;
    white-space: nowrap;
  }
  .contact-icon {
    width: 12px;
    height: 12px;
    flex: none;
  }
</style>
</head>
<body>
<main class="canvas">

  <section class="card card-front" aria-label="Business card front">
    <div class="front-panel">
      <h1 class="brand-name">The Willow Lantern<span class="brand-sub">BOUTIQUE</span></h1>
    </div>
    <p class="holder"><strong>Maren Holloway</strong><span class="divider">|</span>Founder</p>
  </section>

  <section class="card card-back" aria-label="Business card back">
    <div class="contact-band">
      <ul class="contact-list">
        <li>
          <svg class="contact-icon" viewBox="0 0 12 12" aria-hidden="true">
            <circle cx="6" cy="6" r="6" fill="#d8d8d8"/>
            <path d="M6 2.5a2 2 0 0 0-2 2c0 1.6 2 4 2 4s2-2.4 2-4a2 2 0 0 0-2-2z" fill="#3a3939"/>
          </svg>
          Suite # 210, Elm Bldg, NY 10012
        </li>
        <li>
          <svg class="contact-icon" viewBox="0 0 12 12" aria-hidden="true">
            <circle cx="6" cy="6" r="6" fill="#d8d8d8"/>
            <circle cx="6" cy="6" r="3.2" fill="none" stroke="#3a3939" stroke-width="0.9"/>
            <path d="M2.8 6h6.4M6 2.8v6.4" stroke="#3a3939" stroke-width="0.8"/>
          </svg>
          www.thewillowlanternboutique.com
        </li>
        <li>
          <svg class="contact-icon" viewBox="0 0 12 12" aria-hidden="true">
            <circle cx="6" cy="6" r="6" fill="#d8d8d8"/>
            <path d="M4 3l1.2 0 .6 1.5-.8.6a4 4 0 0 0 1.9 1.9l.6-.8 1.5.6V8a1 1 0 0 1-1 1A5 5 0 0 1 3 4a1 1 0 0 1 1-1z" fill="#3a3939"/>
          </svg>
          0400 123 456
        </li>
        <li>
          <svg class="contact-icon" viewBox="0 0 12 12" aria-hidden="true">
            <circle cx="6" cy="6" r="6" fill="#d8d8d8"/>
            <rect x="3" y="4" width="6" height="4.2" fill="none" stroke="#3a3939" stroke-width="0.8"/>
            <path d="M3 4l3 2.4L9 4" fill="none" stroke="#3a3939" stroke-width="0.8"/>
          </svg>
          maren@willowlanternboutique.com.au
        </li>
      </ul>
    </div>
  </section>

</main>
</body>
</html>
```